Stylish new business card needed!

Hello everyone! I am in need of a new business card design for an alarm company here in Hurricane WV. I have all fonts, color codes and logos provided for you use! We are a young company and like the style of a clean sleek looking business card. Would like it double sided, one side holding the logo and the other with your design!
Target Market(s)
The people that are looking for the newest tech for home automation and security
Industry/Entity Type
Alarm services; Home automation
Contact Information for Business Card
Name of person; position (Sales; Installer); Phone Number (555.419.7362); Employee cell Number; Website (www.GuardedByVelm.example); Employee Email; Double sided
Look and feel
Each slider illustrates characteristics of the customer's brand and the style your logo design should communicate.

```html
<!DOCTYPE html>
<html lang="en">
<head>
<meta charset="utf-8">
<title>Velm Business Card</title>
<link href="https://fonts.googleapis.com/css2?family=Montserrat:wght@400;500;700&display=swap" rel="stylesheet">
<style>
  :root {
    --page-bg: #2b2b2b;
    --card-white: #ffffff;
    --card-grey: #999999;
    --brand-orange: #f28c45;
    --text-dark: #3a3a3a;
    --rule-grey: #8a8a8a;
    --logo-grey: #9a9a9a;
  }
  * { margin: 0; padding: 0; box-sizing: border-box; }
  html, body { width: 1200px; height: 900px; overflow: hidden; }
  body {
    background: var(--page-bg);
    font-family: "Montserrat", Arial, sans-serif;
    display: flex;
    flex-direction: column;
    align-items: center;
    justify-content: center;
    gap: 40px;
  }
  .card {
    position: relative;
    width: 700px;
    height: 400px;
    box-shadow: 0 6px 18px rgba(0,0,0,0.45);
  }
  .card--front { background: var(--card-white); }
  .card--back {
    background: var(--card-grey);
    display: flex;
    align-items: center;
    justify-content: center;
  }
  .person { position: absolute; left: 52px; top: 78px; }
  .person__name {
    color: var(--brand-orange);
    font-weight: 700;
    font-size: 27px;
    letter-spacing: 1px;
  }
  .person__title {
    color: var(--text-dark);
    font-size: 15px;
    margin-top: 2px;
  }
  .divider {
    position: absolute;
    left: 40px; right: 50px; top: 160px;
    height: 1px;
    background: var(--rule-grey);
  }
  .contacts {
    position: absolute;
    left: 44px; top: 180px;
    list-style: none;
  }
  .contacts li {
    display: flex;
    align-items: center;
    gap: 9px;
    color: var(--text-dark);
    font-size: 15px;
    height: 28px;
  }
  .contacts svg { width: 14px; height: 14px; fill: var(--brand-orange); }
  .wordmark {
    position: absolute;
    right: 56px; top: 60px;
    display: flex;
    align-items: center;
    gap: 14px;
    font-weight: 500;
    font-size: 72px;
    letter-spacing: 4px;
    color: var(--logo-grey);
  }
  .wordmark__dot {
    width: 22px; height: 22px;
    border-radius: 50%;
    background: var(--brand-orange);
  }
  .address {
    position: absolute;
    right: 56px; bottom: 40px;
    text-align: right;
    color: var(--text-dark);
    font-size: 15px;
    line-height: 1.5;
  }
  .wordmark--back {
    position: static;
    font-size: 120px;
    color: var(--card-white);
    gap: 22px;
  }
  .wordmark--back .wordmark__dot { width: 34px; height: 34px; }
</style>
</head>
<body>
  <section class="card card--front">
    <div class="person">
      <div class="person__name">DANA KELLER</div>
      <div class="person__title">Sales/Installer</div>
    </div>
    <div class="wordmark"><span class="wordmark__dot"></span>VELM</div>
    <div class="divider"></div>
    <ul class="contacts">
      <li>
        <svg viewBox="0 0 16 16" aria-hidden="true"><path d="M3.5 1.5l2.5 0 1.2 3.2-1.6 1.2c.8 1.8 2.2 3.2 4 4l1.2-1.6 3.2 1.2v2.5c0 .8-.7 1.5-1.5 1.5C6.8 13.5 2 8.7 2 3c0-.8.7-1.5 1.5-1.5z"/></svg>
        555.419.7362
      </li>
      <li>
        <svg viewBox="0 0 16 16" aria-hidden="true"><path d="M1 3h14v10H1z M2 4l6 5 6-5" fill="none" stroke="#f28c45" stroke-width="1.6"/></svg>
        info@GuardedByVelm.example
      </li>
      <li>
        <svg viewBox="0 0 16 16" aria-hidden="true"><circle cx="8" cy="8" r="6.5" fill="none" stroke="#f28c45" stroke-width="1.4"/><path d="M1.5 8h13M8 1.5c-3 3.5-3 9.5 0 13M8 1.5c3 3.5 3 9.5 0 13" fill="none" stroke="#f28c45" stroke-width="1.2"/></svg>
        www.GuardedByVelm.example
      </li>
    </ul>
    <div class="address">
      1480 W Harlow Avenue<br>
      Marden County Name 4107
    </div>
  </section>

  <section class="card card--back">
    <div class="wordmark wordmark--back"><span class="wordmark__dot"></span>VELM</div>
  </section>
</body>
</html>
```